1/2 Page add for BRMTL Conference

We are looking for a 1/2 page ad to support the annual BRMTL conference. I want to encourage the attendees to come to our both so we can explain how they can save money on food and supplies. here is a link to the conference. https://www.brmtl-example.org/conference/ here is our website www.pantrywisehub-example.com - the what we do can be captured in the ad. We will be at booth 505. Our goal is to get people to our booth #505 to explain the services that we provide –

Discounted food pricing
Free menu planning/design
Use of Registered Dietitian
Huge selection of discounted PPE and other necessary supplies to run any child care center

We have over 6000 members in 46 States and work with both small and large food distributors. We have been a sponsor of the association for the last 10 years.

Target Market(s)

Child care centers

Requirements
Must have
• Booth number -outline of what we do --- Stress we are a FREE service getting our members reduced pricing on food and supplies

```html
<!DOCTYPE html>
<html lang="en">
<head>
<meta charset="utf-8">
<title>PantryWise Hub – Booth #505 Half Page Ad</title>
<link href="https://fonts.googleapis.com/css2?family=Montserrat:wght@400;600;700;800;900&display=swap" rel="stylesheet">
<style>
  :root {
    --blue: #1f5fa8;
    --blue-dark: #174a86;
    --green: #79b043;
    --green-light: #8cc152;
    --ink: #3a3a3a;
    --paper: #ffffff;
    --canvas: #e9ebee;
    --photo-light: #f4f1ec;
    --photo-mid: #d9dcd8;
    --photo-warm: #e8cfc4;
  }
  * { box-sizing: border-box; margin: 0; padding: 0; }
  html, body { width: 800px; height: 1200px; overflow: hidden; }
  body {
    background: var(--canvas);
    font-family: "Montserrat", Arial, sans-serif;
    color: var(--ink);
    position: relative;
  }
  .ad {
    position: absolute;
    left: 20px; top: 315px;
    width: 760px; height: 570px;
    background: var(--paper);
    overflow: hidden;
    box-shadow: 0 4px 18px rgba(0,0,0,.15);
  }
  .ad__photo {
    position: absolute;
    left: 330px; top: 0; width: 430px; height: 570px;
    background:
      radial-gradient(ellipse at 40% 70%, var(--photo-warm) 0%, transparent 35%),
      radial-gradient(ellipse at 75% 35%, #ffffff 0%, transparent 45%),
      linear-gradient(160deg, var(--photo-light) 0%, var(--photo-mid) 55%, #c9c6bf 100%);
  }
  .ad__content {
    position: absolute; left: 0; top: 0; width: 400px; height: 570px;
    background: var(--paper);
    clip-path: polygon(0 0, 100% 0, 88% 100%, 0 100%);
  }
  .brand {
    position: absolute; left: 30px; top: 26px;
    display: flex; align-items: center; gap: 8px;
    font-weight: 700; font-size: 17px; color: var(--blue);
  }
  .brand__dot { width: 18px; height: 18px; border-radius: 50%; background: var(--green); }
  .headline { position: absolute; left: 30px; top: 78px; color: var(--blue); }
  .headline__lead { font-weight: 800; font-size: 20px; letter-spacing: .5px; }
  .headline__main { font-weight: 900; font-size: 44px; line-height: 1; margin-top: 2px; }
  .headline__booth { font-weight: 900; font-size: 86px; line-height: .95; }
  .services {
    position: absolute; left: 0; top: 245px; width: 360px; height: 112px;
    background: var(--green); color: #fff; padding: 12px 30px;
  }
  .services__title { font-weight: 800; font-size: 12px; letter-spacing: .5px; margin-bottom: 7px; }
  .services__list { list-style: none; font-size: 11px; font-weight: 600; }
  .services__list li { display: flex; align-items: center; gap: 7px; margin-bottom: 4px; }
  .services__list svg { flex: none; }
  .intro {
    position: absolute; left: 30px; top: 368px; width: 300px;
    font-size: 10px; line-height: 1.45; color: #666;
  }
  .stats { position: absolute; left: 30px; top: 410px; display: flex; gap: 32px; }
  .stat__num { font-weight: 900; font-size: 34px; color: var(--blue); line-height: 1; }
  .stat__label { font-size: 11px; font-weight: 600; color: var(--green); }
  .contact-bar {
    position: absolute; left: 0; bottom: 0; width: 470px; height: 92px;
    background: var(--blue); padding: 14px 30px;
    clip-path: polygon(0 0, 100% 0, 88% 100%, 0 100%);
  }
  .contact__phone { color: var(--green-light); font-weight: 800; font-size: 30px; }
  .contact__web { color: #fff; font-weight: 600; font-size: 15px; display: flex; align-items: center; gap: 8px; margin-top: 4px; }
  .accent-strip {
    position: absolute; right: 0; bottom: 0; width: 330px; height: 30px;
    background: var(--green);
    clip-path: polygon(10% 0, 100% 0, 100% 100%, 0 100%);
  }
  .badge {
    position: absolute; left: 470px; top: 24px; width: 150px; height: 150px;
    border-radius: 50%; background: #fff; border: 8px solid var(--blue);
    display: flex; flex-direction: column; align-items: center; justify-content: center;
    text-align: center; padding: 14px; color: var(--blue);
  }
  .badge__lead { font-size: 11px; font-weight: 600; }
  .badge__free { font-size: 38px; font-weight: 900; color: var(--green); line-height: 1; }
  .badge__rest { font-size: 8px; font-weight: 600; line-height: 1.3; }
</style>
</head>
<body>
  <article class="ad">
    <div class="ad__photo" role="img" aria-label="Photo of an elegant banquet room with white-draped tables, place settings and pink floral centrepieces"></div>

    <div class="badge">
      <span class="badge__lead">Stress we are a</span>
      <span class="badge__free">FREE</span>
      <span class="badge__rest">service getting our members reduced pricing on food and supplies</span>
    </div>

    <section class="ad__content">
      <div class="brand"><span class="brand__dot"></span>PantryWise Hub</div>
      <h1 class="headline">
        <div class="headline__lead">TO GET PEOPLE TO</div>
        <div class="headline__main">OUR BOOTH</div>
        <div class="headline__booth">#505</div>
      </h1>
    </section>

    <div class="services">
      <div class="services__title">THE SERVICES THAT WE PROVIDE</div>
      <ul class="services__list">
        <li><svg width="10" height="10" viewBox="0 0 10 10"><path d="M1 5l3 3 5-6" stroke="#fff" stroke-width="2" fill="none"/></svg>Discounted food pricing</li>
        <li><svg width="10" height="10" viewBox="0 0 10 10"><path d="M1 5l3 3 5-6" stroke="#fff" stroke-width="2" fill="none"/></svg>Free menu planning/design</li>
        <li><svg width="10" height="10" viewBox="0 0 10 10"><path d="M1 5l3 3 5-6" stroke="#fff" stroke-width="2" fill="none"/></svg>Use of Registered Dietitian</li>
        <li><svg width="10" height="10" viewBox="0 0 10 10"><path d="M1 5l3 3 5-6" stroke="#fff" stroke-width="2" fill="none"/></svg>Discounted PPE and child care supplies</li>
      </ul>
    </div>

    <p class="intro">We work with both small and large food distributors and have sponsored the association for ten years.</p>

    <div class="stats">
      <div class="stat"><div class="stat__num">6000</div><div class="stat__label">members</div></div>
      <div class="stat"><div class="stat__num">46</div><div class="stat__label">States</div></div>
      <div class="stat"><div class="stat__num">10</div><div class="stat__label">Years</div></div>
    </div>

    <footer class="contact-bar">
      <div class="contact__phone">Call us: 555-014-2290</div>
      <div class="contact__web">
        <svg width="16" height="16" viewBox="0 0 16 16"><circle cx="8" cy="8" r="7" fill="none" stroke="#8cc152" stroke-width="1.6"/><ellipse cx="8" cy="8" rx="3" ry="7" fill="none" stroke="#8cc152" stroke-width="1.2"/><path d="M1 8h14" stroke="#8cc152" stroke-width="1.2"/></svg>
        www.pantrywisehub-example.com
      </div>
    </footer>
    <div class="accent-strip"></div>
  </article>
</body>
</html>
```